Need # Landing Pages

Hi

We need 3 landing pages made must look professional rich design please see website for reference to what we like also in the uploads there are some refrences of some landing pages we thought look ok but are open to any ideas.

1) electrical
2) Generators
3) Remodeling

Must have bushiness logo , phone & pax #
(555) 204- 8193
(555) 731-4620

stock photos ok i like nice rich colors

hear is our web site and email
[url removed, login to view] web site
Info@[url removed, login to view] email

```html
<!DOCTYPE html>
<html lang="en">
<head>
<meta charset="utf-8">
<title>Northwood Renovations and Electrical – Landing Page</title>
<link href="https://fonts.googleapis.com/css2?family=Lato:ital,wght@0,300;0,400;0,700;0,900;1,400&display=swap" rel="stylesheet">
<style>
  :root{
    --orange:#f07c1b;
    --orange-dark:#e06a0c;
    --navy:#34495e;
    --slate:#4a5a6a;
    --ink:#3b4754;
    --muted:#6b7580;
    --pale:#eef1f4;
    --white:#ffffff;
    --hero-a:#6b5a48;
    --hero-b:#3a3630;
    --tile-band:rgba(52,68,86,.88);
    --review-a:#3e5266;
    --review-b:#56687a;
    --green:#4b8a3a;
    --gold:#d8b44a;
  }
  *{box-sizing:border-box;margin:0;padding:0}
  html,body{width:729px;height:1200px;overflow:hidden}
  body{position:relative;font-family:"Lato",sans-serif;color:var(--ink);background:var(--white)}
  .abs{position:absolute}

  /* hero */
  .hero{left:0;top:0;width:729px;height:284px;background:linear-gradient(100deg,var(--hero-a) 0%,#7c6a55 35%,var(--hero-b) 75%,#504a42 100%)}
  .topbar{left:0;top:0;width:729px;height:53px;background:rgba(240,240,240,.92)}
  .brand{left:146px;top:14px;display:flex;align-items:center;gap:6px}
  .brand-mark{width:28px;height:28px;border:2px solid var(--orange);border-radius:4px;background:var(--white)}
  .brand-name{font-size:10.5px;font-weight:900;color:var(--ink);line-height:1.05;letter-spacing:.1px}
  .brand-name small{display:block;font-size:8.5px;font-weight:400;color:var(--ink)}
  .socials{left:395px;top:25px;display:flex;gap:4px}
  .socials span{width:13px;height:13px;border-radius:50%;background:var(--slate)}
  .listing-badge{left:464px;top:15px;width:34px;height:34px;border-radius:3px;background:#2a6aa0}
  .award-badge{left:510px;top:0;width:72px;height:72px;border-radius:50%;background:radial-gradient(circle,#e8cf7a 0%,var(--gold) 60%,#a8842c 100%);border:3px solid var(--green)}

  .hero-title{left:144px;top:77px;font-size:21.5px;font-weight:300;color:var(--white);line-height:1.2}
  .hero-title b{color:var(--orange);font-weight:400}
  .hero-rule{left:146px;top:141px;width:188px;height:1px;background:rgba(255,255,255,.4)}
  .phone{left:146px;display:flex;align-items:center;gap:7px;font-size:20px;font-weight:300;color:var(--orange)}
  .phone .ico{width:27px;height:27px;border:1.5px solid var(--white);border-radius:50%;display:flex;align-items:center;justify-content:center}
  .phone-1{top:154px}
  .phone-2{top:185px}

  .offer{left:331px;top:71px;width:66px;height:66px;border-radius:50%;background:var(--orange);border:2px dashed rgba(255,255,255,.6);color:var(--white);text-align:center}
  .offer .tag{font-size:5px;margin-top:14px;letter-spacing:.3px}
  .offer .num{font-size:24px;font-weight:700;line-height:1}
  .offer .num sup{font-size:11px}
  .offer .num sub{font-size:6px;font-weight:400;vertical-align:0}

  .contact{left:453px;top:88px;width:130px;height:161px;background:var(--orange);padding:15px 15px 0}
  .contact h2{font-size:14px;font-weight:400;color:var(--white);margin-bottom:9px}
  .field{height:13px;background:var(--white);font-size:5px;color:var(--muted);padding:3px 4px;margin-bottom:4px}
  .field.msg{height:29px}
  .submit{margin-top:5px;width:50px;height:15px;border:1px solid var(--white);color:var(--white);font-size:5px;font-weight:700;text-align:center;line-height:13px}
  .scroll-cue{left:356px;top:254px}

  /* services */
  .services-head{left:0;top:310px;width:729px;text-align:center;font-size:13px;font-weight:300;color:var(--slate);line-height:1.3}
  .services-head b{color:var(--orange);font-weight:700}
  .tile{width:101px;height:104px;overflow:hidden}
  .tile .photo{width:101px;height:104px}
  .tile .caption{position:absolute;left:0;bottom:0;width:101px;height:29px;background:var(--tile-band);color:var(--white);font-size:7.3px;line-height:1.3;padding:0 16px 0 7px;display:flex;align-items:center}
  .tile .caption.hot{background:rgba(240,124,27,.92)}
  .tile .caption::after{content:"›";position:absolute;right:7px;top:7px;font-size:11px}

  /* about */
  .about{left:0;top:609px;width:729px;height:293px;background:var(--pale)}
  .about h2{left:0;top:637px;width:729px;text-align:center;font-size:15px;font-weight:400;color:var(--ink)}
  .about-copy{left:146px;top:666px;width:437px;text-align:center;font-size:7px;line-height:13px;color:var(--muted)}
  .laptop-screen{left:165px;top:737px;width:168px;height:111px;background:#222;border-radius:6px;padding:6px}
  .laptop-screen .video{width:100%;height:100%;background:linear-gradient(135deg,#5b4636,#8a7258 50%,#3d3530)}
  .video-title{left:179px;top:749px;font-size:6px;color:#5dc3f0}
  .laptop-base{left:140px;top:848px;width:218px;height:6px;background:linear-gradient(#ddd,#999);border-radius:0 0 8px 8px}
  .guarantee{left:313px;top:830px;width:49px;height:49px;border-radius:50%;background:radial-gradient(circle,#f5d66a,var(--gold) 70%,#b58a22)}
  .checks{left:379px;top:737px;list-style:none;font-size:7.3px;color:var(--muted)}
  .checks li{height:17.3px;display:flex;align-items:center;gap:6px}
  .checks li.more{padding-left:15px}

  /* reviews */
  .reviews{left:0;top:902px;width:729px;height:263px;background:linear-gradient(90deg,var(--review-a),var(--review-b) 60%,#6e7d8a)}
  .reviews h2{left:0;top:931px;width:729px;text-align:center;font-size:15px;font-weight:400;color:var(--white)}
  .avatar{left:338px;top:969px;width:52px;height:52px;border-radius:50%;background:linear-gradient(#c79a78,#8a6a52);border:2px solid var(--white)}
  .nav-btn{top:990px;width:10px;height:10px;background:rgba(255,255,255,.85);font-size:8px;line-height:9px;text-align:center;color:var(--navy)}
  .stars{left:0;top:1025px;width:729px;text-align:center;color:var(--orange);font-size:12px;letter-spacing:1px}
  .quote-mark{left:128px;top:1030px;font-size:30px;color:rgba(255,255,255,.35);font-family:Georgia,serif}
  .quote{left:144px;top:1042px;width:441px;text-align:center;font-size:7px;font-style:italic;color:var(--white);line-height:11px}
  .quote p{margin-bottom:4px}
  .reviewer{left:0;top:1118px;width:729px;text-align:center;font-size:6.5px;font-weight:700;color:var(--orange)}
  .reviewer small{display:block;color:#d4dbe2;font-size:4.5px;font-weight:400;margin-top:3px}

  /* footer */
  .footer{left:0;top:1165px;width:729px;height:35px;background:var(--white)}
  .footer-mark{left:146px;top:1171px;width:22px;height:22px;border:2px solid var(--orange);border-radius:3px}
  .footer-phone{top:1174px;display:flex;align-items:center;gap:5px;font-size:10.5px;color:var(--orange);font-weight:300}
  .footer-phone .ico{width:17px;height:17px;border:1px solid var(--muted);border-radius:50%;display:flex;align-items:center;justify-content:center}
  .footer-socials{left:503px;top:1173px;display:flex;gap:4px}
  .footer-socials span{width:17px;height:17px;border-radius:50%;background:var(--slate)}
</style>
</head>
<body>

<!-- hero -->
<div class="abs hero" role="img" aria-label="Photo of an electrician working on an outdoor electrical panel"></div>
<div class="abs topbar"></div>
<div class="abs brand"><span class="brand-mark"></span><span class="brand-name">NORTHWOOD RENOVATIONS AND ELECTRIC<small>go with the pros cause northwood knows</small></span></div>
<div class="abs socials"><span></span><span></span><span></span><span></span></div>
<div class="abs listing-badge"></div>
<div class="abs award-badge"></div>

<h1 class="abs hero-title">Hire a <b>electrician</b><br>today and save</h1>
<div class="abs hero-rule"></div>
<div class="abs phone phone-1"><span class="ico"><svg width="13" height="13" viewBox="0 0 24 24" fill="none" stroke="#fff" stroke-width="2"><path d="M5 3h4l2 5-3 2a11 11 0 0 0 6 6l2-3 5 2v4a2 2 0 0 1-2 2A17 17 0 0 1 3 5a2 2 0 0 1 2-2z"/></svg></span>(555) 204- 8193</div>
<div class="abs phone phone-2"><span class="ico"><svg width="13" height="13" viewBox="0 0 24 24" fill="none" stroke="#fff" stroke-width="2"><rect x="5" y="3" width="14" height="6"/><rect x="3" y="9" width="18" height="9" rx="1"/><rect x="7" y="14" width="10" height="7"/></svg></span>(555) 731-4620</div>

<div class="abs offer"><div class="tag">SPECIAL OFFER</div><div class="num">40<sup>%</sup><sub>OFF</sub></div></div>

<form class="abs contact">
  <h2>Get in touch</h2>
  <div class="field">Full Name</div>
  <div class="field">E-mail Address</div>
  <div class="field">Phone Number</div>
  <div class="field msg">Message</div>
  <div class="submit">SUBMIT</div>
</form>
<svg class="abs scroll-cue" width="16" height="9" viewBox="0 0 16 9"><path d="M1 1l7 7 7-7" stroke="#fff" stroke-width="1.6" fill="none"/></svg>

<!-- services -->
<h2 class="abs services-head">Our <b>MAPLE RIDGE Commercial and Residential Electrical</b><br>offers all Electrical solutions which includes:</h2>

<div class="abs tile" style="left:146px;top:358px"><div class="photo" role="img" aria-label="Electrician replacing a ceiling light fixture" style="background:linear-gradient(#caa27a,#8c6a4c)"></div><div class="caption hot">Light Fixture Replacement</div></div>
<div class="abs tile" style="left:258px;top:358px"><div class="photo" role="img" aria-label="GFCI outlet with wires" style="background:linear-gradient(#6a4a36,#c8b8a0)"></div><div class="caption">GFCI Outlets</div></div>
<div class="abs tile" style="left:370px;top:358px"><div class="photo" role="img" aria-label="Wall switch plate" style="background:linear-gradient(#8a8c90,#d2d4d6)"></div><div class="caption">New Outlets and Switches</div></div>
<div class="abs tile" style="left:482px;top:358px"><div class="photo" role="img" aria-label="Ceiling fan being installed" style="background:linear-gradient(#3a3028,#a88a68)"></div><div class="caption">Ceiling Fan/Light Installation</div></div>
<div class="abs tile" style="left:146px;top:472px"><div class="photo" role="img" aria-label="Green circuit board" style="background:linear-gradient(#2f7a3a,#1e4f26)"></div><div class="caption">New Circuits</div></div>
<div class="abs tile" style="left:258px;top:472px"><div class="photo" role="img" aria-label="Hand switching circuit breakers" style="background:linear-gradient(#5a5a5c,#c0b8ae)"></div><div class="caption">Tripping Breakers</div></div>
<div class="abs tile" style="left:370px;top:472px"><div class="photo" role="img" aria-label="Electrician upgrading a breaker panel" style="background:linear-gradient(#6e6e70,#9a3a2c)"></div><div class="caption">Panel upgrades</div></div>

<!-- about -->
<div class="abs about"></div>
<h2 class="abs" style="left:0;top:637px;width:729px;text-align:center;font-size:15px;font-weight:400;color:var(--ink)">About Northwood Renovations and Electrical</h2>
<p class="abs about-copy">Your Maple Ridge home runs on electricity but that doesn't matter if the power can't get to where it is supposed to go. Besides having your appliances and fixtures up and running it is equally important that they are efficient, so that you are not spending more money than you should, and that all the wiring is safe. Northwood Renovations And Electrical provides a wide range of electrical services to make sure all the wiring and electrical works in your home are performing as they should.</p>

<div class="abs laptop-screen"><div class="video" role="img" aria-label="Video still of a modern kitchen interior"></div></div>
<div class="abs video-title">How our electrical services works?</div>
<div class="abs laptop-base"></div>
<div class="abs guarantee"></div>

<ul class="abs checks">
  <li><svg width="9" height="7" viewBox="0 0 9 7"><path d="M1 3.5l2.5 2.5L8 1" stroke="#6b7580" fill="none"/></svg>Light Fixture Replacement</li>
  <li><svg width="9" height="7" viewBox="0 0 9 7"><path d="M1 3.5l2.5 2.5L8 1" stroke="#6b7580" fill="none"/></svg>GFCI Outlets</li>
  <li><svg width="9" height="7" viewBox="0 0 9 7"><path d="M1 3.5l2.5 2.5L8 1" stroke="#6b7580" fill="none"/></svg>New Outlets and Switches</li>
  <li><svg width="9" height="7" viewBox="0 0 9 7"><path d="M1 3.5l2.5 2.5L8 1" stroke="#6b7580" fill="none"/></svg>Ceiling Fan/Light Installation</li>
  <li><svg width="9" height="7" viewBox="0 0 9 7"><path d="M1 3.5l2.5 2.5L8 1" stroke="#6b7580" fill="none"/></svg>New Circuits</li>
  <li><svg width="9" height="7" viewBox="0 0 9 7"><path d="M1 3.5l2.5 2.5L8 1" stroke="#6b7580" fill="none"/></svg>Tripping Breakers</li>
  <li><svg width="9" height="7" viewBox="0 0 9 7"><path d="M1 3.5l2.5 2.5L8 1" stroke="#6b7580" fill="none"/></svg>Panel upgrades</li>
  <li class="more">And much more</li>
</ul>

<!-- reviews -->
<div class="abs reviews" role="img" aria-label="Faded photo of a wooden porch"></div>
<h2 class="abs" style="left:0;top:931px;width:729px;text-align:center;font-size:15px;font-weight:400;color:var(--white)">Customer Reviews</h2>
<div class="abs nav-btn" style="left:313px">‹</div>
<div class="abs avatar" role="img" aria-label="Customer portrait"></div>
<div class="abs nav-btn" style="left:406px">›</div>
<div class="abs stars">★★★★★</div>
<div class="abs quote-mark">“</div>
<div class="abs quote">
  <p>Today we had a electrical problem our electrical panel had failed we called northwood renovations and electrical there fast response time was great due to the fact our heat was out with no electrical service.</p>
  <p>My kids where getting cold when they arrived and some how they temped wired our heater in and on it came this relive so much stress off me we will be raving to every one for this one.</p>
  <p>The price was great for a service call like this I thought it was going to cost a lot and it did not I just put it on my credit card life saver</p>
</div>
<div class="abs reviewer">DANA R OAKFIELD IL<small>RESIDENTIAL ELECTRICAL</small></div>

<!-- footer -->
<div class="abs footer"></div>
<div class="abs footer-mark"></div>
<div class="abs footer-phone" style="left:178px"><span class="ico"><svg width="9" height="9" viewBox="0 0 24 24" fill="none" stroke="#6b7580" stroke-width="2"><path d="M5 3h4l2 5-3 2a11 11 0 0 0 6 6l2-3 5 2v4a2 2 0 0 1-2 2A17 17 0 0 1 3 5a2 2 0 0 1 2-2z"/></svg></span>(555) 204- 8193</div>
<div class="abs footer-phone" style="left:285px"><span class="ico"><svg width="9" height="9" viewBox="0 0 24 24" fill="none" stroke="#6b7580" stroke-width="2"><rect x="5" y="3" width="14" height="6"/><rect x="3" y="9" width="18" height="9" rx="1"/><rect x="7" y="14" width="10" height="7"/></svg></span>(555) 731-4620</div>
<div class="abs footer-socials"><span></span><span></span><span></span><span></span></div>

</body>
</html>
```